BRIMLOW Pizza and Wraps

We need a website for a new restaurant called BRIMLOW "PIZZA AND WRAPS".
I have attached fonts, background images, logo, images, content etc.
can provide you with what you need to get the website design done fast and easy

I have uploaded more images of the venue and some menu items. let me know if there is anything I need to provide to make your mission clear and easy

Reason: i would like a little time to provide more feedback to designers

Industry/Entity Type

Restaurant

Coding

Coded - Design and coding required

Number of Pages Required

5+ page

Colors

Designer to choose colors to be used in the design.

Requirements
Must have
• PAGES:
• Our Story
• Menu
• Reservations
• Catering & Delivery
• Contact

```html
<!DOCTYPE html>
<html lang="en">
<head>
<meta charset="utf-8">
<title>Contact — BRIMLOW Pizza and Wraps</title>
<link rel="stylesheet" href="https://fonts.googleapis.com/css2?family=Tinos:wght@400;700&display=swap">
<style>
  :root {
    --brick-light: #b88a72;
    --brick-mid: #9a5f45;
    --brick-dark: #5d3a2c;
    --mortar: #cfc8c2;
    --nav-bg: rgba(248, 246, 245, 0.93);
    --panel-bg: rgba(243, 241, 240, 0.94);
    --form-bg: #ffffff;
    --ink: #1c1c1c;
    --nav-ink: #6a6a6a;
    --rule: #222222;
    --link: #1a73e8;
    --field-border: #ced4da;
    --button-bg: #868e96;
    --map-land: #dfe6cd;
    --map-water: #a9cdf5;
  }
  * { box-sizing: border-box; margin: 0; padding: 0; }
  html, body { width: 1104px; height: 1200px; overflow: hidden; }
  body {
    position: relative;
    font-family: "Tinos", "Times New Roman", serif;
    color: var(--ink);
  }
  .backdrop {
    position: absolute; inset: 0;
    background:
      radial-gradient(ellipse at 20% 85%, rgba(20, 20, 22, 0.75) 0%, rgba(20, 20, 22, 0) 35%),
      radial-gradient(ellipse at 60% 20%, rgba(230, 225, 220, 0.55) 0%, rgba(230, 225, 220, 0) 45%),
      linear-gradient(160deg, var(--brick-mid) 0%, var(--brick-light) 35%, var(--mortar) 55%, var(--brick-mid) 75%, var(--brick-dark) 100%);
  }
  .site-header {
    position: absolute; left: 0; top: 35px; width: 1104px; height: 90px;
    background: var(--nav-bg);
    display: flex; align-items: center; padding: 0 40px;
  }
  .brand {
    font-size: 20px; font-weight: 700; letter-spacing: 3px;
    color: var(--ink); text-decoration: none; white-space: nowrap;
  }
  .site-nav {
    margin-left: auto;
    display: flex; align-items: center; gap: 30px;
  }
  .site-nav a {
    font-size: 14px; letter-spacing: 1.8px; text-decoration: none;
    color: var(--nav-ink); white-space: nowrap;
  }
  .site-nav a.is-current { color: var(--ink); }
  .page-panel {
    position: absolute; left: 77px; top: 151px; width: 953px; height: 1029px;
    background: var(--panel-bg);
  }
  .section-title {
    position: absolute; border-top: 1px solid var(--rule); border-bottom: 1px solid var(--rule);
    text-align: center; font-size: 20px; font-weight: 400;
    display: flex; align-items: center; justify-content: center;
  }
  .contact-title { left: 24px; top: 40px; width: 904px; height: 57px; }
  .map-area {
    position: absolute; left: 24px; top: 113px; width: 593px; height: 334px;
    background: linear-gradient(180deg, var(--map-land) 0%, var(--map-land) 70%, var(--map-water) 100%);
  }
  .contact-info { position: absolute; left: 648px; top: 113px; width: 290px; }
  .info-block { margin-bottom: 21px; }
  .info-block h3 { font-size: 20px; font-weight: 400; line-height: 26px; }
  .info-block p { font-size: 16px; line-height: 25px; }
  .info-block.hours p { line-height: 29px; }
  .info-block a { color: var(--link); text-decoration: none; }
  .form-card {
    position: absolute; left: 24px; top: 507px; width: 904px; height: 474px;
    background: var(--form-bg);
  }
  .form-title { left: 25px; top: 41px; width: 855px; height: 57px; }
  .form-title strong { font-weight: 700; margin-left: 5px; }
  .field { position: absolute; }
  .field label { display: block; font-size: 16px; line-height: 20px; margin-bottom: 12px; }
  .field input, .field textarea {
    display: block; width: 100%; border: 1px solid var(--field-border);
    border-radius: 3px; background: #fff; font: inherit;
  }
  .field input { height: 39px; }
  .field textarea { height: 141px; resize: vertical; }
  .field-name { left: 25px; top: 115px; width: 264px; }
  .field-email { left: 320px; top: 115px; width: 264px; }
  .field-phone { left: 615px; top: 115px; width: 265px; }
  .field-message { left: 25px; top: 203px; width: 855px; }
  .submit-button {
    position: absolute; left: 25px; top: 394px; width: 74px; height: 39px;
    background: var(--button-bg); color: #fff; border: 0; border-radius: 3px;
    font-family: inherit; font-size: 16px; font-weight: 700;
  }
</style>
</head>
<body>
  <div class="backdrop" role="img" aria-label="Photo of a painted brick wall with a coffee mug in the lower left"></div>

  <header class="site-header">
    <a href="#" class="brand">BRIMLOW</a>
    <nav class="site-nav">
      <a href="#">HOME</a>
      <a href="#">OUR STORY</a>
      <a href="#">MENU</a>
      <a href="#">RESERVATIONS</a>
      <a href="#">CATERING &amp; DELIVERY</a>
      <a href="#" class="is-current">CONTACT</a>
    </nav>
  </header>

  <main class="page-panel">
    <h2 class="section-title contact-title">CONTACT</h2>

    <div class="map-area" role="img" aria-label="Embedded road map of the United States showing the restaurant location"></div>

    <aside class="contact-info">
      <div class="info-block">
        <h3>Phone:</h3>
        <p>123.456.7890</p>
      </div>
      <div class="info-block">
        <h3>Email:</h3>
        <p><a href="#">name@example.com</a></p>
      </div>
      <div class="info-block">
        <h3>Address:</h3>
        <p>1234 Larkfield Place</p>
        <p>Ashcombe, CA 90412</p>
      </div>
      <div class="info-block hours">
        <h3>Opening Hours:</h3>
        <p>Daily from: 8am–10pm</p>
        <p>Friday:Closed from Noon–2pm</p>
        <p>Make a reservation</p>
      </div>
    </aside>

    <section class="form-card">
      <h2 class="section-title form-title">CONTACT<strong>FORM</strong></h2>
      <div class="field field-name"><label>Name</label><input type="text"></div>
      <div class="field field-email"><label>Email Address</label><input type="email"></div>
      <div class="field field-phone"><label>Phone Number</label><input type="tel"></div>
      <div class="field field-message"><label>Message</label><textarea></textarea></div>
      <button class="submit-button" type="button">Submit</button>
    </section>
  </main>
</body>
</html>
```